Automobile Review website Requires a stunning Design

Automobiles are an essential part of life and other day-to-day activities and in this vein we are starting up a business website which deal on review of different Automobiles (ranging from cars, trucks, suv, pick up).
The website have to be a "one stop place" for buyers. Our website name is Motor Verdict Hub
Our taste: We dislike template. The design should have some unique elements which helps to distinguish us from competitors. Designs should make a logo along with design.
Required pages:
1. Home - Search cars, News, Reviews, Comparison, Featured cars.
2. Car and Model - This comprises of different cars make, models and features
3. Review page - Detailed analysis and discussions about the different make and model of cars.
NB: We would like to see a mobile size design for the homepage.

```html
<!DOCTYPE html>
<html lang="en">
<head>
<meta charset="utf-8">
<title>Motor Verdict Hub – Home</title>
<link href="https://fonts.googleapis.com/css2?family=Mulish:ital,wght@0,400;0,600;0,700;0,800;1,400&display=swap" rel="stylesheet">
<style>
  :root {
    --white: #ffffff;
    --ink: #1e1e1e;
    --muted: #8a8a8a;
    --line: #d6d6d6;
    --soft-bg: #f2f2f2;
    --brand-blue: #1787bf;
    --caption-blue: #1d86bd;
    --review-bg: #0c271c;
    --review-muted: #6f7f77;
    --star: #2f4a38;
    --footer-bg: #000000;
  }
  * { box-sizing: border-box; margin: 0; padding: 0; }
  html, body {
    width: 1200px; height: 3805px; overflow: hidden;
    background: var(--white);
    font-family: "Mulish", Arial, sans-serif;
    color: var(--ink);
  }
  .page { width: 1200px; height: 3805px; display: flex; flex-direction: column; }

  /* Header */
  .site-header {
    height: 182px; display: flex; align-items: center;
    padding: 0 50px 0 40px; background: var(--white);
  }
  .menu-toggle { display: flex; flex-direction: column; align-items: center; width: 110px; }
  .menu-toggle svg { width: 58px; height: 48px; }
  .menu-toggle span { font-size: 40px; font-weight: 700; line-height: 1; margin-top: 4px; }
  .brand { display: flex; align-items: center; margin-left: 70px; flex: 1; }
  .brand-dot { width: 90px; height: 90px; border-radius: 50%; background: var(--brand-blue); margin-right: 22px; }
  .brand-name { font-size: 60px; font-weight: 600; color: var(--ink); white-space: nowrap; }
  .header-search svg { width: 56px; height: 56px; }

  /* Hero */
  .hero {
    position: relative; height: 653px;
    background: linear-gradient(180deg, #8a6a4a 0%, #c9905a 30%, #6d5a45 55%, #3e3527 80%, #2b251d 100%);
  }
  .hero-copy { position: absolute; left: 80px; top: 190px; color: var(--white); }
  .hero-kicker { font-size: 66px; font-weight: 600; line-height: 1.1; }
  .hero-title { font-size: 132px; font-weight: 600; line-height: 1.15; }
  .hero-dots { position: absolute; left: 0; right: 0; bottom: 50px; display: flex; justify-content: center; gap: 22px; }
  .hero-dots i { width: 26px; height: 26px; border-radius: 50%; background: rgba(255,255,255,0.35); }
  .hero-dots i.active { background: var(--white); }

  /* Search */
  .search-band { height: 289px; display: flex; align-items: center; justify-content: center; background: var(--white); }
  .search-field {
    width: 1025px; height: 120px; border: 3px solid var(--line);
    display: flex; align-items: center; justify-content: space-between; padding: 0 60px 0 72px;
  }
  .search-field span { font-size: 44px; color: var(--muted); }
  .search-field svg { width: 48px; height: 48px; }

  /* Card sections */
  .card-section { background: var(--soft-bg); padding: 40px 91px 0; }
  .news { height: 631px; }
  .featured { height: 624px; background: var(--white); }
  .section-head {
    display: flex; align-items: center; justify-content: space-between;
    border-bottom: 3px solid var(--line); height: 110px;
  }
  .section-head h2 { font-size: 66px; font-weight: 400; }
  .pager { display: flex; gap: 14px; }
  .pager svg { width: 60px; height: 56px; }
  .card-row { display: flex; justify-content: space-between; margin-top: 48px; padding: 0 10px; }
  .card { position: relative; width: 468px; height: 307px; overflow: hidden; }
  .card-image { position: absolute; inset: 0; }
  .img-coast { background: linear-gradient(160deg, #6a7a88 0%, #3b4a5a 45%, #2b6f9e 100%); }
  .img-sunset { background: linear-gradient(160deg, #e9c79c 0%, #c98a5a 45%, #8a4a3a 100%); }
  .img-suv { background: linear-gradient(180deg, #5a4a7a 0%, #8b6a7a 40%, #3a3f6a 100%); }
  .img-forest { background: linear-gradient(150deg, #6da84a 0%, #3f7a2e 50%, #a8b0b4 100%); }
  .card-date {
    position: absolute; top: 0; right: 0; width: 265px; height: 78px;
    background: var(--white); font-size: 33px; font-style: italic;
    display: flex; align-items: center; justify-content: center;
  }
  .card-caption {
    position: absolute; left: 0; right: 0; bottom: 0; height: 122px;
    background: var(--caption-blue); color: var(--white);
    font-size: 34px; font-weight: 700; line-height: 1.35; padding: 10px 50px; text-transform: uppercase;
    display: flex; align-items: center;
  }

  /* Reviews */
  .reviews { height: 674px; background: var(--review-bg); color: var(--white); text-align: center; padding-top: 52px; }
  .reviews h2 { font-size: 64px; font-weight: 400; }
  .review-quote { font-size: 46px; margin-top: 34px; display: flex; justify-content: center; align-items: center; gap: 14px; }
  .quote-mark { color: var(--review-muted); font-size: 70px; font-weight: 800; line-height: 0.6; }
  .review-body { font-size: 37px; color: var(--review-muted); line-height: 1.3; margin: 26px auto 0; width: 1020px; }
  .reviewer { display: flex; align-items: center; justify-content: center; gap: 40px; margin-top: 38px; margin-left: -120px; }
  .reviewer-photo { width: 240px; height: 240px; border-radius: 50%; border: 6px solid #d9d9d9; background: radial-gradient(circle at 50% 40%, #c9a58a 0%, #8a6a55 55%, #e6e6e6 100%); }
  .reviewer-info { text-align: left; }
  .reviewer-name { font-size: 58px; font-weight: 400; }
  .stars { display: flex; gap: 12px; margin-top: 22px; }
  .stars svg { width: 62px; height: 60px; }

  /* Comparison */
  .comparison { height: 612px; background: var(--brand-blue); color: var(--white); text-align: center; padding-top: 80px; }
  .comparison h2 { font-size: 68px; font-weight: 400; letter-spacing: 1px; }
  .comparison-save { font-size: 46px; font-weight: 800; margin-top: 14px; }
  .comparison-save strong { font-size: 82px; }
  .comparison-only { font-size: 44px; font-weight: 800; margin-top: 4px; }
  .btn-more {
    display: inline-flex; align-items: center; justify-content: center;
    width: 538px; height: 125px; margin-top: 56px;
    background: var(--white); color: var(--ink); font-size: 56px; font-weight: 400;
  }

  /* Footer */
  .site-footer {
    height: 140px; background: var(--footer-bg); color: var(--white);
    display: flex; align-items: center; justify-content: center;
    font-size: 31px; font-weight: 600;
  }
</style>
</head>
<body>
<div class="page">

  <header class="site-header">
    <div class="menu-toggle">
      <svg viewBox="0 0 58 48"><rect x="4" y="4" width="50" height="7" fill="#1e1e1e"/><rect x="4" y="20" width="50" height="7" fill="#1e1e1e"/><rect x="4" y="36" width="50" height="7" fill="#1e1e1e"/></svg>
      <span>Menu</span>
    </div>
    <div class="brand">
      <span class="brand-dot"></span>
      <span class="brand-name">Motor Verdict Hub</span>
    </div>
    <div class="header-search">
      <svg viewBox="0 0 56 56"><circle cx="23" cy="23" r="16" fill="none" stroke="#8a8a8a" stroke-width="6"/><line x1="35" y1="35" x2="51" y2="51" stroke="#8a8a8a" stroke-width="7" stroke-linecap="round"/></svg>
    </div>
  </header>

  <section class="hero" role="img" aria-label="Black SUV parked on a rocky shore at sunset with hills and water behind">
    <div class="hero-copy">
      <div class="hero-kicker">One Stop</div>
      <div class="hero-title">Place</div>
    </div>
    <div class="hero-dots"><i class="active"></i><i></i><i></i><i></i></div>
  </section>

  <section class="search-band">
    <div class="search-field">
      <span>Search cars</span>
      <svg viewBox="0 0 48 48"><circle cx="20" cy="20" r="13" fill="none" stroke="#9a9a9a" stroke-width="5"/><line x1="30" y1="30" x2="43" y2="43" stroke="#9a9a9a" stroke-width="6" stroke-linecap="round"/></svg>
    </div>
  </section>

  <section class="card-section news">
    <div class="section-head">
      <h2>News</h2>
      <div class="pager">
        <svg viewBox="0 0 60 56"><rect x="2" y="2" width="56" height="52" fill="#fff" stroke="#b5b5b5" stroke-width="3"/><polyline points="35,16 24,28 35,40" fill="none" stroke="#777" stroke-width="3"/></svg>
        <svg viewBox="0 0 60 56"><rect x="2" y="2" width="56" height="52" fill="#fff" stroke="#b5b5b5" stroke-width="3"/><polyline points="25,16 36,28 25,40" fill="none" stroke="#777" stroke-width="3"/></svg>
      </div>
    </div>
    <div class="card-row">
      <article class="card">
        <div class="card-image img-coast" role="img" aria-label="Car driving along a coastal mountain road"></div>
        <div class="card-date">JAN/23/17</div>
        <div class="card-caption">Lorem ipsum dolor sit amet</div>
      </article>
      <article class="card">
        <div class="card-image img-sunset" role="img" aria-label="Person beside a car in warm evening light"></div>
        <div class="card-date">FEB/23/17</div>
        <div class="card-caption">Lorem ipsum dolor sit amet</div>
      </article>
    </div>
  </section>

  <section class="reviews">
    <h2>Reviews</h2>
    <p class="review-quote"><span class="quote-mark">“</span>Pellentesque convallis molestie enim.</p>
    <p class="review-body">Nullam accumsan purus vel tempus viverra. Mauris suscipit felis id nunc elementum varius. <span class="quote-mark">”</span></p>
    <div class="reviewer">
      <div class="reviewer-photo" role="img" aria-label="Portrait photo of the reviewer"></div>
      <div class="reviewer-info">
        <div class="reviewer-name">John Cole, City</div>
        <div class="stars">
          <svg viewBox="0 0 24 23"><polygon points="12,1 15,8.5 23,9 17,14.5 19,22 12,18 5,22 7,14.5 1,9 9,8.5" fill="var(--star)"/></svg>
          <svg viewBox="0 0 24 23"><polygon points="12,1 15,8.5 23,9 17,14.5 19,22 12,18 5,22 7,14.5 1,9 9,8.5" fill="var(--star)"/></svg>
          <svg viewBox="0 0 24 23"><polygon points="12,1 15,8.5 23,9 17,14.5 19,22 12,18 5,22 7,14.5 1,9 9,8.5" fill="var(--star)"/></svg>
          <svg viewBox="0 0 24 23"><polygon points="12,1 15,8.5 23,9 17,14.5 19,22 12,18 5,22 7,14.5 1,9 9,8.5" fill="var(--star)"/></svg>
          <svg viewBox="0 0 24 23"><polygon points="12,1 15,8.5 23,9 17,14.5 19,22 12,18 5,22 7,14.5 1,9 9,8.5" fill="var(--star)"/></svg>
        </div>
      </div>
    </div>
  </section>

  <section class="comparison">
    <h2>COMPARISON</h2>
    <p class="comparison-save">SAVE UP TO <strong>$2,556</strong></p>
    <p class="comparison-only">ONLY WITH MOTOR VERDICT HUB</p>
    <span class="btn-more">VIEW MORE</span>
  </section>

  <section class="card-section featured">
    <div class="section-head">
      <h2>Featured cars</h2>
      <div class="pager">
        <svg viewBox="0 0 60 56"><rect x="2" y="2" width="56" height="52" fill="#fff" stroke="#b5b5b5" stroke-width="3"/><polyline points="35,16 24,28 35,40" fill="none" stroke="#777" stroke-width="3"/></svg>
        <svg viewBox="0 0 60 56"><rect x="2" y="2" width="56" height="52" fill="#fff" stroke="#b5b5b5" stroke-width="3"/><polyline points="25,16 36,28 25,40" fill="none" stroke="#777" stroke-width="3"/></svg>
      </div>
    </div>
    <div class="card-row">
      <article class="card">
        <div class="card-image img-suv" role="img" aria-label="SUV parked in front of mountains at dusk"></div>
        <div class="card-caption">Lorem ipsum dolor sit amet</div>
      </article>
      <article class="card">
        <div class="card-image img-forest" role="img" aria-label="Rear of a white car on a green forest road"></div>
        <div class="card-caption">Lorem ipsum dolor sit amet</div>
      </article>
    </div>
  </section>

  <footer class="site-footer">© 2017 Motor Verdict Hub. All right reserved.&nbsp; Term of Use</footer>

</div>
</body>
</html>
```